依頼詳細
ホームページのロゴを使いたいです。デリケートな問題ですが、事前に考え、ぜひ終活のお話をきき、
エンディングノートを一緒に書きたくなるような内容。H25年11月、9,10日の産業祭や、ポスティングで使います。
ですが、そこから繋がりができ、御葬儀の依頼をふやしたいです。
終活のイメージは、ホームページのブログの手と手を繋ぐ絵でお願したいです。
記載項目
あおば典礼(ロゴ) キャッチコピー 『大切な人を見送る方々とともに・・・まごころをこめて・・・』
〒317-0088 茨城県日立市緑苑町8-27-3
電話0294-58-7261 FAX0294-43-3540
ホームページ、あおば典礼 検索 フェイスブックページ
御葬儀の内容、金額等
終活相談会の実施、個別、グループで依頼、場所は御自宅、集会所、あおば典礼事務所でも定期的に実施しています。(ホームページ内ブログ、フェイスブックページ、事務所外掲示板、お電話にてご確認下さい。
サイズ
A4
ページ数
両面
希望イメージ
シンプル 複雑
単色 カラフル
暗い 明るい
日常 高級
遊び心 厳粛
未来的 伝統的
女性的 男性的
希望する色
紫、ピンク、
納品ファイル
• 高解像度JPG (.jpg)
補足説明
あおば典礼のホームページ参考にして下さい。
お世話になります。
終活と、御葬儀の宣伝も入れて下さい。

toriyoshiさんの提案は、お葬儀の事と、終活のこと、会社の売り、私どもの気持ちを汲んだ内容が、よくホームページやファイルを読み込んでくれていたと思いました。

お世話になりました。
初めての依頼で要領が分からず、提案しずらかったと思います。
沢山の提案をいただき、自分達が気づかなかった会社の特徴も分かりました。
lanternflyさんには、質問していただいた内容に、すぐに対応して
修正した提案をあげてもらい、ありがたい気持ちです。
会員様へ送っている、瓦版でしたらlanternflyさんの提案が親近感あってよかったと思います。皆さん、きれいに仕上げてくださり ありがとうございました。
また、何か機会がありましたら その時は宜しくお願い申しあげます。

```html
<!DOCTYPE html>
<html lang="ja">
<head>
<meta charset="utf-8">
<title>あおば典礼 終活セミナーのご案内</title>
<link rel="stylesheet" href="https://fonts.googleapis.com/css2?family=Kosugi+Maru&family=Noto+Sans+JP:wght@400;700&display=swap">
<style>
  :root {
    --purple: #8a6aa8;
    --purple-soft: #c9b6dc;
    --pink: #e36a93;
    --pink-soft: #f3c3d4;
    --circle: #f6c6d3;
    --ink: #222;
    --paper: #ffffff;
  }
  * { margin: 0; padding: 0; box-sizing: border-box; }
  html, body { width: 847px; height: 1200px; overflow: hidden; background: var(--paper); }
  .poster {
    position: relative; width: 847px; height: 1200px; overflow: hidden;
    font-family: "Kosugi Maru", "Noto Sans JP", sans-serif; color: var(--ink);
    background: linear-gradient(to bottom, var(--purple) 0, var(--purple-soft) 120px, var(--paper) 330px, var(--paper) 1060px, var(--pink-soft) 1150px, var(--pink) 1200px);
  }
  .headline { position: absolute; left: 0; top: 0; width: 847px; height: 340px; overflow: visible; }
  .headline text { font-family: "Kosugi Maru", sans-serif; fill: var(--ink); }
  .illustration {
    position: absolute; left: 210px; top: 345px; width: 428px; height: 428px;
    border-radius: 50%; background: radial-gradient(circle, #fbe3ea 0, var(--circle) 70%, #eeb0c2 100%);
  }
  .invite {
    position: absolute; top: 780px; width: 100%; text-align: center;
    color: var(--pink); font-size: 19px; line-height: 34px;
  }
  .brand {
    position: absolute; top: 860px; width: 100%;
    display: flex; flex-direction: column; align-items: center; gap: 8px;
  }
  .brand-dot { width: 60px; height: 60px; border-radius: 50%; background: var(--pink); }
  .brand-name { font-size: 34px; color: var(--pink); font-weight: 400; }
  .contact { position: absolute; top: 995px; width: 100%; text-align: center; }
  .contact-note { font-size: 14px; }
  .contact-tel { font-family: "Noto Sans JP", sans-serif; font-weight: 700; font-size: 40px; letter-spacing: 1px; margin-top: 4px; line-height: 1.3; }
  .contact-address { font-size: 12px; margin-top: 2px; line-height: 1.6; }
</style>
</head>
<body>
<div class="poster">
  <svg class="headline" viewBox="0 0 847 340" aria-label="大切な人を見送る方々とともに・・・まごころをこめて・・・">
    <defs><path id="catch-arc" d="M95 325 Q330 165 770 180"/></defs>
    <text font-size="36"><textPath href="#catch-arc" textLength="660" lengthAdjust="spacing">大切な人を見送る方々とともに・・・</textPath></text>
    <text x="300" y="262" font-size="42" textLength="470" lengthAdjust="spacing">まごころをこめて・・・</text>
  </svg>

  <div class="illustration" role="img" aria-label="手と手を繋いで輪になる人々と桜の花のイラスト"></div>

  <p class="invite">終活セミナーで、ちょこっと幸せになりませんか？<br>楽しく　自分らしく　人生ライフを考えエンディングノートに記しませんか？</p>

  <div class="brand">
    <span class="brand-dot"></span>
    <span class="brand-name">あおば典礼</span>
  </div>

  <div class="contact">
    <p class="contact-note">仏事に関する事、お墓を問わずお気軽にお電話ください。</p>
    <p class="contact-tel">TEL. 0294-58-7261</p>
    <p class="contact-address">〒317-0088 茨城県日立市緑苑町8-27-3<br>ホームページ http://www.aobatenrei.jp</p>
  </div>
</div>
</body>
</html>
```